Brightpath Tutors Homepage and Landing Page Redesign

Brightpath Tutors 456 is a premier test preparation, academic consultation, and private tutoring company based in Los Angeles. We offer our tutoring in-person and also online. <br/><br/>We will need three mockups that are as follows:<br/><br/>1. A mockup of a homepage that will be on www.brightpathtutors456.com<br/>2. A mockup of a free-standing true landing page that will be a one-page site where we will direct traffic from a Zindle PPC ad.<br/>3. A mockup of a landing page that will replace a landing page such as the one at www.brightpathtutors456.com/test-prep-services/k-12/sat/ <br/><br/>Please see the word attached for details.

Target Market(s)

Middle School and High School Student Parents, College Students.

Industry/Entity Type

Tutoring

Number of Pages Required

3 page

Colors

Designer to choose colors to be used in the design.

Requirements
Must have
• The design of these 3 pages will need to fit within the overall design of the main website. We're looking for a user-friendly, easy-to-navigate, yet professional design.

```html
<!DOCTYPE html>
<html lang="en">
<head>
<meta charset="utf-8">
<title>Brightpath Tutors – Learning as easy as 123</title>
<link rel="stylesheet" href="https://fonts.googleapis.com/css2?family=Josefin+Sans:wght@600;700&family=Titillium+Web:wght@600;700&family=Open+Sans:wght@400;600&display=swap">
<style>
:root{
  --teal:#2b95a9;
  --teal-dark:#237f91;
  --ink:#333a3f;
  --text:#555;
  --muted:#777;
  --dark:#323538;
  --white:#fff;
}
*{box-sizing:border-box;margin:0;padding:0}
html,body{width:1200px;height:4373px;overflow:hidden}
body{position:relative;font-family:"Open Sans",sans-serif;color:var(--text);background:var(--white)}
.abs{position:absolute}
.heading{font-family:"Titillium Web",sans-serif;font-weight:700;color:var(--teal);text-align:center;text-transform:uppercase;letter-spacing:.5px}
.divider{position:absolute;left:50%;width:76px;height:2px;margin-left:-38px;background:var(--ink)}
.divider::after{content:"";position:absolute;left:50%;top:-3px;width:8px;height:8px;margin-left:-4px;border-radius:50%;background:var(--ink)}
.divider.light{background:#fff}.divider.light::after{background:#fff}
.btn{position:absolute;background:var(--teal);color:#fff;font-size:13px;text-align:center;letter-spacing:.5px}

/* top bar & nav */
.topbar{left:0;top:0;width:1200px;height:37px;background:var(--teal);color:#fff;font-size:11px}
.topbar span{position:absolute;top:11px;display:flex;align-items:center;gap:8px;white-space:nowrap}
.nav{left:0;top:37px;width:1200px;height:77px;border-bottom:1px solid rgba(255,255,255,.2);z-index:3}
.nav a{position:absolute;top:0;height:76px;line-height:76px;color:#fff;font-size:11px;text-decoration:none;text-align:center;border-left:1px solid rgba(255,255,255,.2)}
.brand{position:absolute;color:#fff;font-family:"Josefin Sans",sans-serif;font-weight:700;text-align:center}

/* hero */
.hero-photo{left:0;top:0;width:1200px;height:712px;background:linear-gradient(180deg,#2c3033 0%,#4d4a45 45%,#7a6d62 75%,#8c8780 100%);clip-path:polygon(0 0,100% 0,100% 90%,50% 100%,0 90%)}
.hero-frame{left:294px;top:272px;width:611px;height:220px;border:3px solid var(--teal);border-top:none;border-bottom:none}
.hero-frame::before,.hero-frame::after{content:"";position:absolute;top:0;width:36px;height:3px;background:var(--teal)}
.hero-frame::before{left:0}.hero-frame::after{right:0}
.hero-title{left:294px;top:264px;width:611px;color:#fff;font-family:"Josefin Sans",sans-serif;font-weight:700;font-size:31px;line-height:50px;text-align:center;text-transform:uppercase;white-space:nowrap}
.hero-sub{left:294px;top:374px;width:611px;color:#fff;font-size:14px;line-height:22px;text-align:center}

/* featured */
.featured{left:0;top:620px;width:1200px;height:565px;background:linear-gradient(180deg,#c9ccd0 0%,#e3e4e5 25%,#eceae5 55%,#cdb9a0 82%,#5f8b98 100%);z-index:-1}
.skyline{left:0;top:960px;width:1200px;height:225px;background:linear-gradient(180deg,rgba(95,120,130,0) 0%,rgba(80,115,125,.55) 40%,#3f7f8f 100%)}
.press{top:865px;font-size:21px;color:#8a8e92;font-weight:600}

/* why choose us */
.hexagon{left:468px;top:1354px;width:272px;height:428px;background:linear-gradient(160deg,#c79a62 0%,#9b6e42 45%,#d28f2c 100%);clip-path:polygon(50% 0,100% 15%,100% 85%,50% 100%,0 85%,0 15%)}
.service .icon{position:absolute;width:92px;height:92px;border-radius:50%;background:#fff;box-shadow:0 2px 10px rgba(0,0,0,.12);display:flex;align-items:center;justify-content:center}
.service h3{position:absolute;font-family:"Titillium Web",sans-serif;font-size:15px;font-weight:600;color:var(--teal);text-transform:uppercase;white-space:nowrap}
.service p{position:absolute;width:190px;font-size:11px;line-height:19px;color:var(--muted)}
.service .more{position:absolute;font-size:11px;font-weight:600;color:var(--teal)}
.right h3,.right p,.right .more{text-align:right}

/* results */
.results{left:0;top:1855px;width:1200px;height:606px;background:linear-gradient(180deg,#2d3a40 0%,#3b4347 40%,#4d4a44 80%,#5b5448 100%);clip-path:polygon(0 0,100% 0,100% 88%,50% 100%,0 88%)}
.stat{position:absolute;width:202px;height:262px;background:#fff}
.stat .photo{position:absolute;left:0;top:0;width:202px;height:140px;clip-path:polygon(0 0,100% 0,100% 72%,50% 100%,0 72%)}
.stat .num{position:absolute;left:69px;top:106px;width:64px;height:64px;border-radius:50%;background:var(--teal);border:3px solid #fff;color:#fff;font-weight:600;font-size:17px;line-height:58px;text-align:center}
.stat h4{position:absolute;top:178px;width:100%;text-align:center;color:var(--teal);font-size:14px;font-weight:600}
.stat p{position:absolute;top:204px;left:22px;width:158px;text-align:center;font-size:10.5px;line-height:17px;color:#444}

/* steps */
.step{position:absolute;top:2678px;width:278px;height:260px;background:#fff;box-shadow:0 1px 8px rgba(0,0,0,.1)}
.step h4{position:absolute;top:124px;width:100%;text-align:center;color:var(--teal);font-size:14px;font-weight:600;line-height:22px;text-transform:uppercase}
.step p{position:absolute;top:176px;left:28px;width:222px;text-align:center;font-size:10.5px;line-height:18px;color:var(--muted)}
.step .go{position:absolute;left:120px;top:241px;width:38px;height:38px;border-radius:50%;background:var(--teal);display:flex;align-items:center;justify-content:center}

/* team */
.member{position:absolute;top:3182px;width:190px;text-align:center}
.member .portrait{height:198px;border-bottom:2px solid var(--teal);background:linear-gradient(180deg,#f4f5f6 0%,#e6e9ec 100%)}
.member h4{margin-top:20px;color:var(--teal);font-size:14px;font-weight:600}
.member .spec{color:var(--teal);font-size:10.5px;margin-top:2px}
.member p{color:var(--muted);font-size:10.5px;line-height:18px;margin-top:2px;white-space:nowrap}

/* contact */
.band-dark{left:0;top:3615px;width:1200px;height:758px;background:var(--dark)}
.band-teal{left:0;top:3615px;width:1200px;height:320px;background:var(--teal);clip-path:polygon(0 0,100% 0,100% 90%,50% 70%,0 98%)}
.pitch{left:150px;top:3640px;width:900px;text-align:center;color:#fff;font-size:23px;line-height:38px}
.form{left:300px;top:3747px;width:600px;height:390px;background:#fff}
.field{position:absolute;height:52px;background:var(--teal);color:#fff;font-size:12px;line-height:52px;padding-left:12px}
.footer-links{left:0;top:4272px;width:1200px;text-align:center;color:#bbb;font-size:11px}
.footer-links span{margin:0 20px}
.footer-rule{left:0;top:4324px;width:1200px;height:1px;background:rgba(255,255,255,.12)}
.copy{left:0;top:4343px;width:1200px;text-align:center;color:#9a9a9a;font-size:10px}
</style>
</head>
<body>

<!-- hero -->
<div class="abs hero-photo" role="img" aria-label="Photo of two students studying at an outdoor table"></div>
<div class="abs topbar">
  <span style="left:162px"><svg width="12" height="14" viewBox="0 0 12 16"><path d="M6 0a6 6 0 0 0-6 6c0 4.5 6 10 6 10s6-5.5 6-10a6 6 0 0 0-6-6zm0 8.5A2.5 2.5 0 1 1 6 3.5a2.5 2.5 0 0 1 0 5z" fill="#fff"/></svg>1820 Palmcrest Ave. Suite 300 Los Angeles, CA 90099</span>
  <span style="left:718px"><svg width="13" height="10" viewBox="0 0 13 10"><rect width="13" height="10" fill="#fff"/><path d="M0 0l6.5 5L13 0" stroke="#2b95a9" fill="none"/></svg>contact@brightpathtutors456.com</span>
  <span style="left:950px"><svg width="11" height="11" viewBox="0 0 24 24"><path d="M6.6 10.8a15 15 0 0 0 6.6 6.6l2.2-2.2c.3-.3.7-.4 1-.2 1.1.4 2.3.6 3.6.6.6 0 1 .4 1 1V20c0 .6-.4 1-1 1A17 17 0 0 1 3 4c0-.6.4-1 1-1h3.5c.6 0 1 .4 1 1 0 1.3.2 2.5.6 3.6.1.3 0 .7-.2 1z" fill="#fff"/></svg>213-555-0147</span>
</div>
<nav class="abs nav">
  <a style="left:161px;width:80px">HOME</a>
  <a style="left:241px;width:162px">ACADAMIC SUPPORT</a>
  <a style="left:403px;width:107px">TEST PREP</a>
  <a style="left:735px;width:87px">ABOUT</a>
  <a style="left:822px;width:115px">RESOURCES</a>
  <a style="left:937px;width:103px;border-right:1px solid rgba(255,255,255,.2)">CONTACT</a>
  <div class="brand" style="left:510px;top:16px;width:225px;font-size:24px;line-height:26px">BRIGHTPATH</div>
  <div class="brand" style="left:510px;top:44px;width:225px;font-size:11px;font-weight:600;letter-spacing:1px">Learning as easy as 123</div>
</nav>
<div class="abs hero-frame"></div>
<h1 class="abs hero-title">Brightpath Tutors learning as<br>easy as 123</h1>
<p class="abs hero-sub">Experienced, professional tutors available for private sessions<br>either in-home in Los Angeles or online, worldwide.</p>
<div class="btn" style="left:468px;top:475px;width:263px;height:34px;line-height:34px">Schedule Your Free Consultation</div>
<svg class="abs" style="left:580px;top:608px" width="40" height="28" viewBox="0 0 40 28"><path d="M2 2l18 12L38 2M2 13l18 12 18-12" stroke="#fff" stroke-width="2" fill="none"/></svg>

<!-- featured -->
<div class="abs featured"></div>
<div class="abs skyline" role="img" aria-label="City skyline at dusk"></div>
<h2 class="abs heading" style="left:0;top:762px;width:1200px;font-size:38px">Featured In</h2>
<div class="divider" style="top:818px"></div>
<svg class="abs" style="left:70px;top:862px" width="16" height="30" viewBox="0 0 16 30"><path d="M14 2L2 15l12 13" stroke="#555" stroke-width="2" fill="none"/></svg>
<svg class="abs" style="left:1112px;top:862px" width="16" height="30" viewBox="0 0 16 30"><path d="M2 2l12 13L2 28" stroke="#555" stroke-width="2" fill="none"/></svg>
<span class="abs press" style="left:162px">Metro Daily</span>
<span class="abs press" style="left:360px">KBN</span>
<span class="abs press" style="left:464px">NewsLoft</span>
<span class="abs press" style="left:620px">Skillwise</span>
<span class="abs press" style="left:780px">Ledgerline</span>
<span class="abs press" style="left:924px">howPedia</span>

<!-- why choose us -->
<h2 class="abs heading" style="left:0;top:1250px;width:1200px;font-size:38px">Why Choose Us</h2>
<div class="divider" style="top:1308px"></div>
<div class="abs hexagon" role="img" aria-label="Photo of a student writing in a library"></div>

<div class="service">
  <div class="icon" style="left:161px;top:1427px"><svg width="36" height="34" viewBox="0 0 36 34"><path d="M4 2h28a3 3 0 0 1 3 3v18a3 3 0 0 1-3 3H14l-8 7v-7H4a3 3 0 0 1-3-3V5a3 3 0 0 1 3-3z" fill="#2b95a9"/><circle cx="11" cy="14" r="2.3" fill="#fff"/><circle cx="18" cy="14" r="2.3" fill="#fff"/><circle cx="25" cy="14" r="2.3" fill="#fff"/></svg></div>
  <h3 style="left:270px;top:1434px">Academic Tutoring</h3>
  <p style="left:270px;top:1464px">Work with one of our expert tutors to supplement what you're learning in school.</p>
  <span class="more" style="left:270px;top:1526px">Learn More ➞</span>
</div>
<div class="service">
  <div class="icon" style="left:161px;top:1583px"><svg width="26" height="34" viewBox="0 0 26 34"><path d="M2 1h16l7 7v25H2z" fill="#2b95a9"/><path d="M7 12h12M7 17h12M7 22h12M7 27h8" stroke="#fff" stroke-width="2"/></svg></div>
  <h3 style="left:270px;top:1590px">K-12 / College Test Prep</h3>
  <p style="left:270px;top:1620px">Work one-on-one with one of our veteran tutors to help you achieve your test prep goals.</p>
  <span class="more" style="left:270px;top:1682px">Learn More ➞</span>
</div>
<div class="service right">
  <div class="icon" style="left:947px;top:1427px"><svg width="46" height="34" viewBox="0 0 46 34"><path d="M23 2L1 12l22 10 22-10z" fill="#2b95a9"/><path d="M10 17v9c4 4 22 4 26 0v-9l-13 6z" fill="#2b95a9"/><path d="M41 13v12" stroke="#2b95a9" stroke-width="2"/></svg></div>
  <h3 style="left:742px;top:1434px;width:190px">Graduate Test Prep</h3>
  <p style="left:742px;top:1464px">Prepare for your graduate-level exam with one of our tutors and customize.</p>
  <span class="more" style="left:742px;top:1526px;width:190px">Learn More ➞</span>
</div>
<div class="service right">
  <div class="icon" style="left:947px;top:1583px"><svg width="34" height="30" viewBox="0 0 34 30"><rect x="1" y="7" width="32" height="22" rx="2" fill="#2b95a9"/><path d="M12 7V3h10v4" stroke="#2b95a9" stroke-width="2.5" fill="none"/><path d="M1 15h32" stroke="#fff" stroke-width="1.5"/><rect x="14" y="13" width="6" height="5" fill="#fff"/></svg></div>
  <h3 style="left:742px;top:1590px;width:190px">Professional Test</h3>
  <p style="left:742px;top:1620px">Connect with a specialist who can work around your and help you pass</p>
  <span class="more" style="left:742px;top:1682px;width:190px">Learn More ➞</span>
</div>

<!-- proven results -->
<div class="abs results" role="img" aria-label="Photo of a historic university building"></div>
<h2 class="abs" style="left:0;top:1886px;width:1200px;text-align:center;color:#fff;font-size:29px;font-weight:600">Proven Results From a Tutoring Company You Can Trust</h2>
<div class="divider light" style="top:1943px"></div>
<p class="abs" style="left:290px;top:1966px;width:620px;text-align:center;color:#fff;font-size:12px;line-height:23px">Brightpath Tutors only works with highly experienced, professional, veteran tutors who have a proven track record of success. Our individualized approach has helped countless students achieve the academic and test prep goals of their dreams.</p>

<div class="stat" style="left:161px;top:2077px">
  <div class="photo" role="img" aria-label="Photo of graduates in caps and gowns" style="background:linear-gradient(180deg,#8a8f96,#3a3d42)"></div>
  <div class="num">150</div><h4>SAT</h4>
  <p>Our students average a 150 point increase on the SAT.</p>
</div>
<div class="stat" style="left:387px;top:2136px">
  <div class="photo" role="img" aria-label="Photo of students holding certificates" style="background:linear-gradient(180deg,#7d3a35,#3b2a2a)"></div>
  <div class="num">4</div><h4>ACT</h4>
  <p>Our students average a 4 point increase on the ACT.</p>
</div>
<div class="stat" style="left:611px;top:2077px">
  <div class="photo" role="img" aria-label="Photo of a campus quad" style="background:linear-gradient(180deg,#7ea6c4,#8f7658 60%,#4f6b3a)"></div>
  <div class="num">2.5</div><h4>ISEE</h4>
  <p>Our students average a 2.5 stanine improvement on the ISEE.</p>
</div>
<div class="stat" style="left:837px;top:2136px">
  <div class="photo" role="img" aria-label="Photo of students in a school library" style="background:linear-gradient(180deg,#b9a785,#7c8a9a)"></div>
  <div class="num">90%</div><h4>CSET</h4>
  <p>Over 90% of our students pass the CSET.</p>
</div>
<svg class="abs" style="left:580px;top:2440px" width="40" height="28" viewBox="0 0 40 28"><path d="M2 2l18 12L38 2M2 13l18 12 18-12" stroke="#fff" stroke-width="2" fill="none"/></svg>

<!-- easy as 1-2-3 -->
<h2 class="abs heading" style="left:0;top:2575px;width:1200px;font-size:38px">It's as easy as 1-2-3</h2>
<div class="divider" style="top:2634px"></div>

<div class="step" style="left:161px">
  <svg class="abs" style="left:106px;top:14px" width="66" height="90" viewBox="0 0 66 90"><path d="M8 14l25-12 25 12-25 10z" fill="#2b95a9"/><path d="M33 24c-20 0-30 14-30 32 0 20 14 32 30 32s30-12 30-32c0-18-10-32-30-32z" fill="#a8d3dc"/><text x="33" y="66" text-anchor="middle" font-family="Titillium Web,sans-serif" font-size="30" fill="#fff">01</text></svg>
  <h4>Answer a few questions<br>about your needs</h4>
  <p>When you enroll, one of our program coordinators will call you to discuss your needs.</p>
  <div class="go"><svg width="16" height="12" viewBox="0 0 16 12"><path d="M1 6h12M9 1l5 5-5 5" stroke="#fff" stroke-width="2" fill="none"/></svg></div>
</div>
<div class="step" style="left:461px">
  <svg class="abs" style="left:106px;top:14px" width="66" height="90" viewBox="0 0 66 90"><path d="M8 14l25-12 25 12-25 10z" fill="#2b95a9"/><path d="M33 24c-20 0-30 14-30 32 0 20 14 32 30 32s30-12 30-32c0-18-10-32-30-32z" fill="#a8d3dc"/><text x="33" y="66" text-anchor="middle" font-family="Titillium Web,sans-serif" font-size="30" fill="#fff">02</text></svg>
  <h4>We match you with the<br>perfect tutor</h4>
  <p>One of the most crucial parts of working with a tutor is ensuring that it's a right fit. Once we understand what type of tutor.</p>
  <div class="go"><svg width="16" height="12" viewBox="0 0 16 12"><path d="M1 6h12M9 1l5 5-5 5" stroke="#fff" stroke-width="2" fill="none"/></svg></div>
</div>
<div class="step" style="left:761px">
  <svg class="abs" style="left:106px;top:14px" width="66" height="90" viewBox="0 0 66 90"><path d="M8 14l25-12 25 12-25 10z" fill="#2b95a9"/><path d="M33 24c-20 0-30 14-30 32 0 20 14 32 30 32s30-12 30-32c0-18-10-32-30-32z" fill="#a8d3dc"/><text x="33" y="66" text-anchor="middle" font-family="Titillium Web,sans-serif" font-size="30" fill="#fff">03</text></svg>
  <h4>Schedule your first<br>session</h4>
  <p>We can schedule your lessons in-person, online, or even in a café/library if you prefer.</p>
  <div class="go"><svg width="16" height="12" viewBox="0 0 16 12"><path d="M1 6h12M9 1l5 5-5 5" stroke="#fff" stroke-width="2" fill="none"/></svg></div>
</div>
<div class="btn" style="left:524px;top:2988px;width:151px;height:36px;line-height:36px">ENROLL TODAY</div>

<!-- team -->
<h2 class="abs heading" style="left:0;top:3092px;width:1200px;font-size:38px">Meet Our Team</h2>
<div class="divider" style="top:3151px"></div>
<div class="member" style="left:163px"><div class="portrait" role="img" aria-label="Portrait of tutor Lena M."></div><h4>LENA M.</h4><div class="spec">Specializes in ACT</div><p>Northbrook College<br>B.E in Mechanical Engineering</p></div>
<div class="member" style="left:391px"><div class="portrait" role="img" aria-label="Portrait of tutor Owen P."></div><h4>OWEN P.</h4><div class="spec">Specializes in HSPT</div><p>Ridgefield University<br>B.A. in Literature</p></div>
<div class="member" style="left:615px"><div class="portrait" role="img" aria-label="Portrait of tutor Clara S."></div><h4>CLARA S.</h4><div class="spec">Specializes in SAT</div><p>Lakemont University<br>B.A. in Politics</p></div>
<div class="member" style="left:850px"><div class="portrait" role="img" aria-label="Portrait of tutor Marcus T."></div><h4>MARCUS T.</h4><div class="spec">Specializes in ISEE</div><p>Westvale Institute of Technology<br>Ph.D. candidate</p></div>
<div class="btn" style="left:524px;top:3502px;width:151px;height:36px;line-height:36px">ENROLL TODAY</div>

<!-- contact -->
<div class="abs band-dark"></div>
<div class="abs band-teal"></div>
<p class="abs pitch">Our elite team of tutors has been helping students realize their academic potential for over a decade. Let us do the same for you.</p>
<form class="abs form">
  <h3 class="heading" style="position:absolute;left:0;top:28px;width:600px;font-size:22px;line-height:30px">Schedule a free<br>consultation today</h3>
  <div class="field" style="left:37px;top:133px;width:172px">Name</div>
  <div class="field" style="left:212px;top:133px;width:172px">E-mail</div>
  <div class="field" style="left:388px;top:133px;width:175px">Phone</div>
  <div class="field" style="left:37px;top:193px;width:526px">Schhol Name</div>
  <div class="field" style="left:37px;top:253px;width:526px">Home Zip Code</div>
  <div class="btn" style="left:244px;top:336px;width:112px;height:36px;line-height:36px;font-size:12px">SEND</div>
</form>

<!-- footer -->
<div class="brand abs" style="left:450px;top:4190px;width:300px;font-size:28px;line-height:30px">BRIGHTPATH</div>
<div class="brand abs" style="left:450px;top:4224px;width:300px;font-size:13px;font-weight:600;letter-spacing:1px">Learning as easy as 123</div>
<div class="abs footer-links"><span>HOME</span>|<span>ACADAMIC SUPPORT</span>|<span>TEST PREP</span>|<span>ABOUT</span>|<span>RESOURCES</span>|<span>CONTACT</span></div>
<div class="abs footer-rule"></div>
<p class="abs copy">©Brightpath Tutors learning as easy as – 2020 All Rights Reserved.</p>

</body>
</html>
```